Update our business cards to match our awesome new website

Need a new design for company business cards. We have recently revamped our website and would like our business cards to get a refresh too. I've uploaded the company artwork, logo, as well as the Branding Deck to better understand the look & feel of our brand. Please visit the website at bellcrestholdingsoh.com.

Industry/Entity Type

Real Estate

Contact Information for Business Card

must use the colors outlined in the Branding Deck uploaded to the site, or the colors of our logo.

Font styles to use
Other font styles liked:
• Calibri

Requirements
Must have
• Required items: Name, title, company logo, address: 217 Fennimore Ave. Suite 300, Lakeport, OH 44093, email address: glen@bellcrestholdingsOH.com, company phone 800-555-0172, cell: 216-555-0148
Nice to have
• a more simple design. not complicated
Should not have
• cartoonish characters, or whimsical writing or artwork, stay within our branding colors

```html
<!DOCTYPE html>
<html lang="en">
<head>
<meta charset="utf-8">
<title>Bellcrest Holdings – Business Cards</title>
<link href="https://fonts.googleapis.com/css2?family=Carlito:wght@400;700&display=swap" rel="stylesheet">
<style>
  :root {
    --bg: #e4e5e7;
    --paper: #fbfbfb;
    --green: #2fb589;
    --green-dark: #1d8a5b;
    --ink: #2b2b2b;
    --ink-soft: #3d3d3d;
  }
  * { box-sizing: border-box; margin: 0; padding: 0; }
  html, body { width: 1200px; height: 1000px; overflow: hidden; }
  body {
    background: var(--bg);
    font-family: "Carlito", "Calibri", sans-serif;
    position: relative;
  }
  .card {
    position: absolute;
    width: 560px;
    height: 320px;
    background: var(--paper);
    box-shadow: 0 6px 18px rgba(0,0,0,0.12);
    overflow: hidden;
  }

  /* Front */
  .card--front { left: 70px; top: 150px; }
  .front-art { position: absolute; inset: 0; }
  .front-brand {
    position: absolute;
    left: 0; right: 0; top: 150px;
    display: flex; align-items: center; justify-content: center; gap: 10px;
  }

  /* Back */
  .card--back { left: 570px; top: 530px; }
  .back-edge {
    position: absolute; right: 0; top: 0; bottom: 0;
    width: 16px; background: var(--green-dark);
  }
  .person { position: absolute; left: 232px; top: 58px; }
  .person__name {
    font-weight: 700; font-size: 30px; letter-spacing: 1px;
    color: var(--green-dark); line-height: 1;
  }
  .person__title { font-weight: 700; font-size: 12px; color: var(--green-dark); margin-top: 3px; }

  .contacts {
    position: absolute; left: 200px; top: 122px;
    display: grid; grid-template-columns: 190px 140px; column-gap: 10px; row-gap: 10px;
    font-size: 11px; color: var(--ink-soft); line-height: 1.3;
  }
  .contact { display: flex; align-items: flex-start; gap: 8px; }
  .contact svg { flex: none; width: 12px; height: 12px; margin-top: 1px; }

  .back-brand {
    position: absolute; left: 44px; bottom: 56px;
    display: flex; align-items: center; gap: 9px;
  }

  .brand-dot { width: 14px; height: 14px; border-radius: 50%; background: var(--green); flex: none; }
  .brand-name {
    font-weight: 400; font-size: 26px; color: var(--ink);
    letter-spacing: 0.5px; white-space: nowrap;
  }
  .back-brand .brand-name { font-size: 22px; }
</style>
</head>
<body>

<section class="card card--front" aria-label="Business card front">
  <svg class="front-art" viewBox="0 0 560 320" width="560" height="320" aria-hidden="true">
    <rect x="0" y="0" width="560" height="16" fill="var(--green)"/>
    <path d="M0 160 H90 A190 130 0 0 0 470 160 H560 V320 H0 Z" fill="var(--green)"/>
  </svg>
  <div class="front-brand">
    <span class="brand-dot"></span>
    <span class="brand-name">Bellcrest Holdings of Ohio, LLC</span>
  </div>
</section>

<section class="card card--back" aria-label="Business card back">
  <div class="back-edge"></div>

  <div class="person">
    <div class="person__name">JON DOE</div>
    <div class="person__title">Lorem Ipsum</div>
  </div>

  <div class="contacts">
    <div class="contact">
      <svg viewBox="0 0 12 12" aria-hidden="true"><path d="M6 0.5a4 4 0 0 0-4 4c0 3 4 7 4 7s4-4 4-7a4 4 0 0 0-4-4z" fill="var(--green)"/><circle cx="6" cy="4.5" r="1.5" fill="#fff"/></svg>
      <span>217 Fennimore Ave. Suite 300,<br>Lakeport, OH 44093</span>
    </div>
    <div class="contact">
      <svg viewBox="0 0 12 12" aria-hidden="true"><rect x="3" y="0.5" width="6" height="11" rx="1.2" fill="none" stroke="var(--green)" stroke-width="1.2"/><line x1="5" y1="9.5" x2="7" y2="9.5" stroke="var(--green)"/></svg>
      <span>216-555-0148</span>
    </div>
    <div class="contact">
      <svg viewBox="0 0 12 12" aria-hidden="true"><rect x="0.6" y="2" width="10.8" height="8" fill="none" stroke="var(--green)" stroke-width="1.2"/><path d="M0.6 2.5 L6 6.5 L11.4 2.5" fill="none" stroke="var(--green)" stroke-width="1.2"/></svg>
      <span>glen@bellcrestholdingsOH.com</span>
    </div>
    <div class="contact">
      <svg viewBox="0 0 12 12" aria-hidden="true"><circle cx="6" cy="6" r="5.2" fill="none" stroke="var(--green)" stroke-width="1.2"/><ellipse cx="6" cy="6" rx="2.2" ry="5.2" fill="none" stroke="var(--green)"/><line x1="0.8" y1="6" x2="11.2" y2="6" stroke="var(--green)"/></svg>
      <span>bellcrestholdingsoh.com</span>
    </div>
    <div class="contact">
      <svg viewBox="0 0 12 12" aria-hidden="true"><path d="M2.5 0.8 L4.6 3.3 L3.5 4.8 C4.3 6.6 5.4 7.7 7.2 8.5 L8.7 7.4 L11.2 9.5 L9.8 11.2 C5 10.6 1.4 7 0.8 2.2 Z" fill="var(--green)"/></svg>
      <span>800-555-0172</span>
    </div>
  </div>

  <div class="back-brand">
    <span class="brand-dot"></span>
    <span class="brand-name">Bellcrest Holdings of Ohio, LLC</span>
  </div>
</section>

</body>
</html>
```